The Visual Personality of Miss Paprika Food Trailer

Something that stands out with color and our logo. This is a food trailer that attends several events in the spring and summer. We are known for being one of the best Gumbo producers in mid Michigan. We have been responsible for connecting different communities and cultures together and we are strong supporters of our veterans since this is a veteran owned business. All of our vegetables are fresh and locally purchased. These recipes are originally from New Orleans Louisiana. Our website is Misspaprika.com. This will be used for an 8" x 11" poster. Leave a box or area that states "WHERE WE WILL BE:" so that we can add the location of the event that we are attending.

Target Market(s)

We do cuisine that is recognized in the southern states of the USA. but live in the northern part of the USA. We are providing a menu of different southern recipes so they do not have to go all the way down south for get..

Industry/Entity Type

Food/Restaurant Industry

Font styles to use
Serif
Decorative

Colors
0094D4
00A9DD
6FCCEA
C7EBF8
E9F6FB
59FF00
82FF00
B8FF75
E3FFCB
F4FFEA
FFF300
FFF600
FEFA6F
FFFEC7
FFFEE8
EE7325
F08F49
F5BC92
FAE3D3
FDF4ED
EB3D1F
EC4F4E
F09395
F8D3D4
FCEDEE
A7469A
B969AE
D3A5CF
EDDBEB
F8F0F9

Requirements
Must have
• Our logo, which is "Miss Paprika", "Homemade Deliciousness". We need an area on the poster where we can manually add the location of the event we will be attending because it changes weekly. location
Nice to have
• Bold colors and logo

```html
<!DOCTYPE html>
<html lang="en">
<head>
<meta charset="utf-8">
<title>Miss Paprika Food Trailer Poster</title>
<link rel="stylesheet" href="https://fonts.googleapis.com/css2?family=Bree+Serif&display=swap">
<style>
  :root {
    --cream: #f7f6f1;
    --ring-red: #e30a1c;
    --ink-brown: #4a3a33;
    --hours-red: #d10f28;
    --box-orange: #f58a22;
    --address-tint: #f9ab60;
    --white: #ffffff;
    --logo-ink: #1f1f1f;
  }
  * { margin: 0; padding: 0; box-sizing: border-box; }
  html, body { width: 848px; height: 1200px; overflow: hidden; background: var(--cream); }
  .poster {
    position: relative;
    width: 848px;
    height: 1200px;
    overflow: hidden;
    background: var(--cream);
    font-family: "Bree Serif", Georgia, serif;
  }
  .dish-rings { position: absolute; inset: 0; }
  .brand {
    position: absolute;
    left: 508px;
    top: 150px;
    width: 282px;
    text-align: center;
    color: var(--logo-ink);
    font-size: 52px;
    line-height: 1.05;
    letter-spacing: 2px;
  }
  .mission {
    position: absolute;
    left: 297px;
    top: 494px;
    width: 486px;
    color: var(--ink-brown);
    font-size: 16px;
    line-height: 33px;
    letter-spacing: 3px;
    text-align: justify;
    text-transform: uppercase;
  }
  .location-box {
    position: absolute;
    left: 274px;
    top: 722px;
    width: 535px;
    height: 201px;
    border-radius: 28px;
    background: var(--box-orange);
  }
  .location-title {
    position: absolute;
    left: 30px;
    top: 44px;
    color: var(--white);
    font-size: 22px;
    letter-spacing: 1px;
  }
  .location-address {
    position: absolute;
    left: 0;
    right: 0;
    top: 104px;
    text-align: center;
    color: var(--address-tint);
    font-size: 21px;
    letter-spacing: 3px;
  }
  .hours {
    position: absolute;
    left: 286px;
    top: 956px;
    width: 400px;
    text-align: center;
    color: var(--hours-red);
    font-size: 27px;
    line-height: 40px;
  }
</style>
</head>
<body>
<main class="poster">
  <svg class="dish-rings" width="848" height="1200" viewBox="0 0 848 1200">
    <defs>
      <radialGradient id="soup-tone" cx="50%" cy="50%" r="50%">
        <stop offset="0%" stop-color="#d9643a"/>
        <stop offset="75%" stop-color="#c4552f"/>
        <stop offset="100%" stop-color="#e6e6ea"/>
      </radialGradient>
      <linearGradient id="flatbread-tone" x1="0" y1="0" x2="1" y2="1">
        <stop offset="0%" stop-color="#d9c9a0"/>
        <stop offset="100%" stop-color="#b9a56e"/>
      </linearGradient>
      <linearGradient id="poboy-tone" x1="0" y1="0" x2="0" y2="1">
        <stop offset="0%" stop-color="#e2dcd2"/>
        <stop offset="100%" stop-color="#c9843f"/>
      </linearGradient>
      <linearGradient id="burger-tone" x1="0" y1="0" x2="0" y2="1">
        <stop offset="0%" stop-color="#5a4030"/>
        <stop offset="100%" stop-color="#b97a3c"/>
      </linearGradient>
    </defs>

    <circle class="ring" cx="195" cy="206" r="200" fill="var(--ring-red)"/>
    <circle cx="176" cy="186" r="178" fill="var(--white)"/>
    <circle cx="176" cy="186" r="172" fill="url(#soup-tone)" role="img" aria-label="Photo of a bowl of gumbo"/>

    <circle class="ring" cx="22" cy="670" r="150" fill="var(--ring-red)"/>
    <circle cx="8" cy="670" r="128" fill="var(--white)"/>
    <circle cx="8" cy="670" r="122" fill="url(#flatbread-tone)" role="img" aria-label="Photo of a shrimp flatbread"/>

    <circle class="ring" cx="152" cy="1160" r="190" fill="var(--ring-red)"/>
    <circle cx="152" cy="1184" r="160" fill="var(--white)"/>
    <circle cx="152" cy="1184" r="154" fill="url(#poboy-tone)" role="img" aria-label="Photo of a po'boy sandwich with chips"/>

    <circle class="ring" cx="782" cy="1183" r="168" fill="var(--ring-red)"/>
    <circle cx="790" cy="1200" r="146" fill="var(--white)"/>
    <circle cx="790" cy="1200" r="140" fill="url(#burger-tone)" role="img" aria-label="Photo of a club sandwich with fries"/>

    <rect x="388" y="295" width="72" height="66" rx="20" fill="#fbe9a8" opacity="0.6" role="img" aria-label="Yellow sparkles"/>
    <rect x="388" y="1150" width="72" height="66" rx="20" fill="#fbe9a8" opacity="0.6" role="img" aria-label="Yellow sparkles"/>
    <rect x="180" y="420" width="100" height="170" rx="40" fill="#cfe6c4" opacity="0.7" role="img" aria-label="Cilantro sprigs"/>
    <rect x="85" y="820" width="180" height="95" rx="40" fill="#f4c3a0" opacity="0.7" role="img" aria-label="Red and orange chili peppers"/>
    <rect x="690" y="870" width="130" height="100" rx="40" fill="#d8edc2" opacity="0.7" role="img" aria-label="Green bell pepper rings"/>
  </svg>

  <div class="brand">Miss<br>Paprika</div>

  <p class="mission">We prepare and serve amazing high quality, delicious southern food at an affordable price. We want to provide our customers with the most authentic Louisiana experience outside of Louisiana.</p>

  <section class="location-box">
    <h2 class="location-title">WHERE WE WILL BE</h2>
    <p class="location-address">YOUR ADDRESS HERE</p>
  </section>

  <p class="hours">Monday, Friday, Saturday<br>11:00 am EST - 3 pm EST</p>
</main>
</body>
</html>
```